New Business Card for General Contractor Marketing

Need a business card the is more like a marketing promotion of our services
Must be horizontal orientation, One Sided Only, Max font size, Organize the Services
#1 General Contractor for Realtors
Remodels – Renovations – Repairs
Water & Mold Damage Experts
Painting: Interior/ Exterior
Flooring: Wood / LVT / Carpet
Plumbing: Repairs & Upgrades
Electric: Lights & Energy Efficient Upgrades
Kitchen & Bath Remodels
Fast Inspections Repair Billed Thru Escrow
BrightHarborBuilds.com
555-418-2796

Industry/Entity Type

General Contractor

Contact Information for Business Card

One Sided Only: #1 General Contractor for Realtors Remodels – Renovations – Repairs Water & Mold Damage Experts Painting: Interior/ Exterior Flooring: Wood / LVT / Carpet Plumbing: Repairs & Upgrades Electric: Lights & Energy Efficient Upgrades Kitchen & Bath Remodels Fast Inspections Repair Billed Thru Escrow BrightHarborBuilds.com 555-418-2796

Colors
0054AA
0677BA
7BADD7
CADEEF
E8F1F8

Requirements
Must have
• One Sided Only: #1 General Contractor for Realtors Remodels – Renovations – Repairs Water & Mold Damage Experts Painting: Interior/ Exterior Flooring: Wood / LVT / Carpet Plumbing: Repairs & Upgrades Electric: Lights & Energy Efficient Upgrades Kitchen & Bath Remodels Fast Inspections Repair Billed Thru Escrow BrightHarborBuilds.com 555-418-2796

```html
<!DOCTYPE html>
<html lang="en">
<head>
<meta charset="utf-8">
<title>Bright Harbor Builds – Business Card</title>
<link href="https://fonts.googleapis.com/css2?family=Montserrat:wght@400;500;600;700;800&display=swap" rel="stylesheet">
<style>
  :root {
    --navy: #0054AA;
    --blue: #0677BA;
    --sky: #7BADD7;
    --pale: #CADEEF;
    --mist: #E8F1F8;
    --periwinkle: #6F7FC8;
    --white: #FFFFFF;
    --stage: #A9C6E3;
  }
  * { box-sizing: border-box; margin: 0; padding: 0; }
  html, body { width: 1200px; height: 876px; overflow: hidden; }
  body {
    background: var(--stage);
    font-family: "Montserrat", Arial, sans-serif;
    display: flex; align-items: center; justify-content: center;
  }
  .card {
    width: 1050px; height: 600px;
    background: var(--white);
    display: flex; flex-direction: column;
    box-shadow: 0 14px 40px rgba(0, 50, 110, 0.25);
    overflow: hidden;
  }
  .tagline-band {
    height: 70px;
    background: linear-gradient(90deg, var(--blue), var(--navy));
    color: var(--white);
    display: flex; align-items: center; justify-content: center;
    font-size: 34px; font-weight: 500; letter-spacing: 1px;
  }
  .brand-area {
    flex: 1;
    display: flex; flex-direction: column; align-items: center; justify-content: center;
    gap: 14px;
  }
  .brand-name {
    display: flex; align-items: center; gap: 16px;
    color: var(--navy);
    font-size: 58px; font-weight: 800; text-transform: uppercase; letter-spacing: 1px;
  }
  .brand-mark { width: 30px; height: 30px; background: var(--sky); }
  .brand-claim {
    color: var(--navy); font-size: 26px; font-weight: 500;
  }
  .services-band {
    height: 140px;
    background: linear-gradient(90deg, var(--periwinkle) 0%, var(--sky) 55%, var(--pale) 100%);
    display: flex; justify-content: space-between;
    padding: 20px 60px;
    color: var(--white);
    font-size: 22px; font-weight: 500; line-height: 1.5;
  }
  .services-list { list-style: none; }
  .contact-band {
    height: 130px;
    background: linear-gradient(90deg, var(--navy), var(--blue));
    color: var(--white);
    display: flex; justify-content: space-between; align-items: center;
    padding: 0 60px;
  }
  .contact-details { font-size: 28px; font-weight: 700; line-height: 1.45; }
  .escrow-offer {
    font-size: 34px; font-weight: 700; text-align: right; line-height: 1.3;
  }
</style>
</head>
<body>
  <article class="card">
    <header class="tagline-band">Remodels – Renovations – Repairs</header>
    <section class="brand-area">
      <div class="brand-name"><span class="brand-mark"></span>BrightHarborBuilds</div>
      <p class="brand-claim">— #1 General Contractor for Realtors —</p>
    </section>
    <section class="services-band">
      <ul class="services-list">
        <li>Water &amp; Mold Damage Experts</li>
        <li>Painting: Interior/ Exterior</li>
        <li>Flooring: Wood / LVT / Carpet</li>
      </ul>
      <ul class="services-list">
        <li>Plumbing: Repairs &amp; Upgrades</li>
        <li>Electric: Lights &amp; Energy Efficient Upgrades</li>
        <li>Kitchen &amp; Bath Remodels</li>
      </ul>
    </section>
    <footer class="contact-band">
      <div class="contact-details">
        <p class="website">www.BrightHarborBuilds.com</p>
        <p class="phone">555-418-2796</p>
      </div>
      <p class="escrow-offer">Fast Inspections Repair<br>Billed Thru Escrow</p>
    </footer>
  </article>
</body>
</html>
```